Create Vertical Dog Food Labels (3 inches x 5 inches) for PupKitchen

We need a packing Vertical label (3 inches x 5 inches) design for our line of Dog Food - Pup Kitchen at pupkitchenmeals.com (please review website). This design is for Custom Roll Labels. We have a logo already. Use our logo colors on label. What we need incorporated is a list of our ingredients:

50% Choice Beef
20% Pasture-raised Chicken
15% Brown Rice
15% Fresh Vegetables - Carrots, Kale, Zucchini
Herbal Health Boosters

We also need these lines at the bottom of the label:

Keeps in fridge for 4 days after thawing
Stores in freezer up to 6 months
Questions? email us at orders@meadowlanepantry.com

We have attached a sample of a competitor. The Kibble Crate.

Target Market(s)

Dog owners

Industry/Entity Type

Dog Food

Font styles to use
Sans Serif

Requirements
Must have
• Read project description above
Nice to have
• Our logo color incorporated
Should not have
• I want it simple.

```html
<!DOCTYPE html>
<html lang="en">
<head>
<meta charset="utf-8">
<title>PupKitchen – Vertical Dog Food Label</title>
<link rel="stylesheet" href="https://fonts.googleapis.com/css2?family=Open+Sans:wght@600&family=Roboto+Condensed:wght@300;400;700&display=swap">
<style>
  :root {
    --backdrop: #c6c4c5;
    --paper: #ffffff;
    --leaf-green: #5b9f39;
    --forest-green: #166a30;
    --pill-green: #1f7536;
    --ink-green: #17692f;
    --storage-ink: #1a5429;
    --sun-orange: #f4a51c;
    --white: #ffffff;
  }
  html, body {
    margin: 0;
    padding: 0;
    width: 857px;
    height: 1200px;
    overflow: hidden;
    background: var(--backdrop);
  }
  .label {
    position: absolute;
    left: 68px;
    top: 0;
    width: 721px;
    height: 1200px;
    background: var(--paper);
  }
  .label svg { display: block; }
  .brand-name {
    font-family: "Open Sans", sans-serif;
    font-weight: 600;
    font-size: 54px;
    letter-spacing: 3px;
    fill: var(--ink-green);
  }
  .brand-dot { fill: var(--leaf-green); }
  .ingredient-share {
    font-family: "Roboto Condensed", sans-serif;
    font-weight: 700;
    font-size: 40px;
    fill: var(--leaf-green);
  }
  .ingredient-name {
    font-family: "Roboto Condensed", sans-serif;
    font-weight: 700;
    font-size: 40px;
    fill: var(--ink-green);
  }
  .ingredient-detail {
    font-family: "Roboto Condensed", sans-serif;
    font-weight: 300;
    font-size: 30px;
    fill: var(--ink-green);
  }
  .ingredient-rule { stroke: var(--leaf-green); stroke-width: 1.5; }
  .hill-light { fill: var(--leaf-green); }
  .hill-dark { fill: var(--forest-green); }
  .sun { fill: var(--sun-orange); }
  .storage-title {
    font-family: "Roboto Condensed", sans-serif;
    font-weight: 700;
    font-size: 33px;
    fill: var(--storage-ink);
  }
  .storage-marker { fill: var(--storage-ink); }
  .storage-line {
    font-family: "Roboto Condensed", sans-serif;
    font-weight: 300;
    font-size: 29px;
    fill: var(--white);
  }
  .storage-line .emph { font-weight: 700; }
  .contact-heading {
    font-family: "Roboto Condensed", sans-serif;
    font-weight: 700;
    font-size: 52px;
    fill: var(--white);
  }
  .contact-lead {
    font-family: "Roboto Condensed", sans-serif;
    font-weight: 400;
    font-size: 27px;
    fill: var(--white);
  }
  .contact-pill { fill: var(--pill-green); }
  .contact-email {
    font-family: "Roboto Condensed", sans-serif;
    font-weight: 700;
    font-size: 29px;
    fill: var(--white);
  }
</style>
</head>
<body>
<div class="label">
  <svg width="721" height="1200" viewBox="0 0 721 1200" xmlns="http://www.w3.org/2000/svg">
    <!-- Brand -->
    <g class="brand">
      <circle class="brand-dot" cx="160" cy="141" r="40"/>
      <text class="brand-name" x="230" y="161">PupKitchen</text>
    </g>

    <!-- Ingredients -->
    <g class="ingredients">
      <line class="ingredient-rule" x1="235" y1="278" x2="235" y2="660"/>
      <text class="ingredient-share" x="216" y="322" text-anchor="end">50%</text>
      <text class="ingredient-name" x="253" y="322">Choice Beef</text>
      <text class="ingredient-share" x="216" y="392" text-anchor="end">20%</text>
      <text class="ingredient-name" x="253" y="392">Pasture-raised Chicken</text>
      <text class="ingredient-share" x="216" y="462" text-anchor="end">15%</text>
      <text class="ingredient-name" x="253" y="462">Brown Rice</text>
      <text class="ingredient-share" x="216" y="532" text-anchor="end">15%</text>
      <text class="ingredient-name" x="253" y="532">Fresh Vegetables</text>
      <text class="ingredient-detail" x="254" y="571">Carrots, Kale, Zucchini</text>
      <text class="ingredient-share" x="216" y="637" text-anchor="end">&amp;</text>
      <text class="ingredient-name" x="253" y="637">Herbal Health Boosters</text>
    </g>

    <!-- Landscape -->
    <path class="hill-light" d="M0 658 C190 708 380 790 558 891 L721 831 L721 1200 L0 1200 Z"/>
    <path class="hill-dark" d="M76 1200 C220 1060 390 950 558 893 C620 920 680 950 721 975 L721 1200 Z"/>
    <path class="sun" d="M496 847 C530 800 595 800 626 851 L558 880 Z"/>

    <!-- Storage -->
    <g class="storage">
      <text class="storage-title" x="61" y="787">Storage</text>
      <path class="storage-marker" d="M61 802 L94 802 L77.5 813 Z"/>
      <text class="storage-line" x="61" y="850">Keeps in FRIDGE</text>
      <text class="storage-line" x="61" y="884">for <tspan class="emph">4 days</tspan> after thawing</text>
      <path class="storage-marker" d="M61 905 L94 905 L77.5 916 Z"/>
      <text class="storage-line" x="59" y="951">Stores in FREEZER up</text>
      <text class="storage-line" x="59" y="985">to <tspan class="emph">6 months</tspan></text>
    </g>

    <!-- Contact -->
    <g class="contact">
      <text class="contact-heading" x="669" y="1039" text-anchor="end">Questions?</text>
      <text class="contact-lead" x="664" y="1071" text-anchor="end">Email us at</text>
      <rect class="contact-pill" x="222" y="1084" width="463" height="72" rx="36"/>
      <text class="contact-email" x="453" y="1131" text-anchor="middle">orders@meadowlanepantry.com</text>
    </g>
  </svg>
</div>
</body>
</html>
```